KBMR new business card design

We need a business card design for our established business which is Australia wide however based in Melbourne. We are a young team of Financial Planners who specialize in Insurance and Basic super advice for people like us.

We are people who help our clients get things done in a timely and cost effective manner whilst having a good time and a laugh along the way.

We would like this to have a consistent feel with our new e-brochure which i have attached from a color and font perspective.

Industry/Entity Type

Business

Requirements
Must have
• We do not need specific address details rather just the states we are in:

VIC/NSW/QLD/TAS
Nice to have
• Curved edge to mate the brochure

```html
<!DOCTYPE html>
<html lang="en">
<head>
<meta charset="utf-8">
<title>KBMR Planning – Business Card Set</title>
<link rel="stylesheet" href="https://fonts.googleapis.com/css2?family=Arimo:ital,wght@0,400;0,700;1,700&family=PT+Sans&display=swap">
<style>
  :root {
    --stage: #e9e6e2;
    --card-white: #ffffff;
    --card-dark: #1b1b1b;
    --card-dark-2: #2a2a2a;
    --green-deep: #0f9a4a;
    --green-leaf: #6cc04a;
    --ink: #111111;
    --ink-soft: #3a3a3a;
    --grey-text: #6f6f6f;
    --label: #2b2b2b;
  }
  * { margin: 0; padding: 0; box-sizing: border-box; }
  html, body { width: 1200px; height: 788px; overflow: hidden; }
  body {
    position: relative;
    background: var(--stage);
    font-family: "Arimo", Arial, sans-serif;
  }
  .view-label {
    position: absolute;
    width: 526px;
    text-align: center;
    font-family: "PT Sans", sans-serif;
    font-size: 22px;
    color: var(--label);
  }
  .card {
    position: absolute;
    width: 526px;
    height: 300px;
    border-radius: 22px;
    overflow: hidden;
    background: var(--card-white);
    box-shadow: 0 4px 10px rgba(0,0,0,0.18);
  }
  .card--dark {
    background: linear-gradient(160deg, var(--card-dark-2), var(--card-dark));
  }
  .swoosh { position: absolute; }
  .brand {
    position: absolute;
    text-align: center;
  }
  .brand__mark {
    display: block;
    margin: 0 auto 18px;
    background: var(--green-leaf);
    border-radius: 14px;
  }
  .brand__name {
    font-weight: 700;
    color: var(--ink);
    white-space: nowrap;
    line-height: 1.05;
  }
  .card--dark .brand__name { color: #ffffff; }
  .divider {
    position: absolute;
    width: 2px;
    background: linear-gradient(to bottom, rgba(120,120,120,0), rgba(120,120,120,0.8) 50%, rgba(120,120,120,0));
  }
  .contact { position: absolute; color: var(--ink-soft); }
  .contact__name { font-size: 18px; font-weight: 700; color: var(--ink-soft); }
  .contact__role { font-size: 13px; font-weight: 700; line-height: 17px; }
  .contact__list { list-style: none; margin-top: 20px; font-size: 13.5px; }
  .contact__list li { height: 25.5px; }
  .contact__list em { font-weight: 700; font-style: italic; }
  .services { position: absolute; }
  .services__title {
    font-size: 18px; font-weight: 700; font-style: italic;
    color: var(--grey-text); margin-bottom: 12px;
  }
  .services__list { list-style: none; font-size: 14px; font-weight: 700; color: var(--grey-text); }
  .services__list li { height: 34px; }
  .services__list li::before { content: "▪ "; font-size: 11px; }
  .services--centered { text-align: center; }
  .services--centered .services__title,
  .services--centered .services__list { color: #444; }
  .card--dark .services__title,
  .card--dark .services__list { color: #ffffff; }
  .tagline-band {
    position: absolute; left: 0; right: 0; bottom: 0; height: 39px;
    background: var(--green-leaf); color: #fff;
    font-size: 14.5px; font-weight: 700; text-align: center; line-height: 39px;
  }
  .tagline {
    position: absolute; font-size: 14.5px; font-weight: 700; color: #444;
  }
  .tagline--green { color: var(--green-leaf); line-height: 18px; }
</style>
</head>
<body>

  <!-- Front -->
  <div class="view-label" style="left:52px; top:32px;">Front</div>
  <section class="card" style="left:52px; top:72px;">
    <svg class="swoosh" width="526" height="300" viewBox="0 0 526 300" aria-hidden="true">
      <path d="M410 0 Q490 10 526 48 L526 30 Q500 6 460 0 Z" fill="var(--green-leaf)"/>
      <path d="M430 0 Q500 18 526 60 L526 48 Q490 10 410 0 Z" fill="var(--green-deep)"/>
      <path d="M0 255 Q60 290 140 300 L90 300 Q30 285 0 268 Z" fill="var(--green-leaf)"/>
      <path d="M0 268 Q30 285 90 300 L60 300 Q20 290 0 280 Z" fill="var(--green-deep)"/>
    </svg>
    <div class="brand" style="left:62px; top:52px; width:160px;">
      <span class="brand__mark" style="width:110px; height:110px;"></span>
      <div class="brand__name" style="font-size:30px;">KBMR<br>Planning</div>
    </div>
    <div class="divider" style="left:260px; top:28px; height:250px;"></div>
    <div class="contact" style="left:290px; top:44px;">
      <div class="contact__name">Daniel Harrow</div>
      <div class="contact__role">ADFS, BBus, LRS©<br>Financial Adviser</div>
      <ul class="contact__list">
        <li><em>cell</em> 0400 555 218</li>
        <li><em>phone</em> 1300 555 864</li>
        <li><em>fax</em> 03 9555 0417</li>
        <li><em>email</em> daniel@kbmr.com.au</li>
        <li><em>web</em> www.kbmr.com.au</li>
        <li>VIC/NSW/QLD/TAS</li>
      </ul>
    </div>
  </section>

  <!-- Back 1 -->
  <div class="view-label" style="left:622px; top:32px;">Back - 1</div>
  <section class="card" style="left:622px; top:74px;">
    <div class="brand" style="left:62px; top:52px; width:160px;">
      <span class="brand__mark" style="width:100px; height:100px;"></span>
      <div class="brand__name" style="font-size:28px;">KBMR<br>Planning</div>
    </div>
    <div class="divider" style="left:260px; top:22px; height:235px;"></div>
    <div class="services" style="left:320px; top:46px;">
      <div class="services__title">Specialising in</div>
      <ul class="services__list">
        <li>Risk Insurance</li>
        <li>Debt Management</li>
        <li>Superannuation</li>
        <li>Wealth Creation</li>
        <li>Retirement Planning</li>
      </ul>
    </div>
    <div class="tagline-band">SECURE FUTURE, ENHANCED LIFESTYLE</div>
  </section>

  <!-- Back 2 -->
  <div class="view-label" style="left:54px; top:403px;">Back - 2</div>
  <section class="card" style="left:54px; top:446px;">
    <div class="services services--centered" style="left:0; width:526px; top:46px;">
      <div class="services__title">Specialising in</div>
      <ul class="services__list">
        <li>Risk Insurance</li>
        <li>Debt Management</li>
        <li>Superannuation</li>
        <li>Wealth Creation</li>
        <li>Retirement Planning</li>
      </ul>
    </div>
    <div class="tagline" style="left:0; width:526px; text-align:center; top:267px;">SECURE FUTURE, ENHANCED LIFESTYLE</div>
  </section>

  <!-- Back 3 -->
  <div class="view-label" style="left:622px; top:403px;">Back - 3</div>
  <section class="card card--dark" style="left:622px; top:446px;">
    <div class="brand" style="left:52px; top:30px; width:200px;">
      <span class="brand__mark" style="width:150px; height:150px;"></span>
      <div class="brand__name" style="font-size:34px;">KBMR<br>Planning</div>
    </div>
    <div class="services" style="left:314px; top:26px;">
      <div class="services__title">Specialising in</div>
      <ul class="services__list">
        <li>Risk Insurance</li>
        <li>Debt Management</li>
        <li>Superannuation</li>
        <li>Wealth Creation</li>
        <li>Retirement Planning</li>
      </ul>
    </div>
    <div class="tagline tagline--green" style="left:313px; top:252px;">SECURE FUTURE<br>ENHANCED LIFESTYLE</div>
  </section>

</body>
</html>
```